Green Energy Conservation Business Cards

We believe in Conserve before you produce energy. I am looking for a unique, bold business card. that Demonstrates Expertise in our field. I would be interested to try and incorporate a night picture of the US or world showing the yellow lights on one side. I would be open to a design that caters to half the business card size height and same length. Our primary expertise is Energy projects for self storage. Use either black or white background .Attached are the logos and symbols.

May I see some design utilizing a smaller business card. the same length as a normal business card but cut in half on the height. best regards Garrick

```html
<!DOCTYPE html>
<html lang="en">
<head>
<meta charset="utf-8">
<title>Solvane Energy Group – Business Cards</title>
<link rel="stylesheet" href="https://fonts.googleapis.com/css2?family=Exo+2:wght@400;500;600&display=swap">
<style>
  :root {
    --backdrop: #9b9b9b;
    --card: #ffffff;
    --brand-blue: #1565b0;
    --brand-green: #7dc243;
    --ink: #2b2b2b;
    --title-blue: #2f7cc4;
  }
  * { box-sizing: border-box; margin: 0; padding: 0; }
  html, body { width: 1200px; height: 894px; overflow: hidden; }
  body {
    background: var(--backdrop);
    font-family: "Exo 2", sans-serif;
    display: flex;
    align-items: center;
    justify-content: center;
    gap: 40px;
  }
  .card {
    position: relative;
    width: 540px;
    height: 309px;
    background: var(--card);
    overflow: hidden;
  }
  .brand {
    display: flex;
    align-items: center;
    gap: 10px;
    color: var(--brand-blue);
    font-weight: 600;
    font-size: 26px;
    white-space: nowrap;
  }
  .brand-dot {
    width: 34px; height: 34px;
    border-radius: 50%;
    background: var(--brand-green);
    flex: none;
  }
  /* contact side */
  .card-back .brand { position: absolute; left: 24px; top: 34px; }
  .divider {
    position: absolute; left: 0; top: 104px;
    width: 330px; height: 2px;
    background: var(--brand-blue);
  }
  .person { position: absolute; right: 28px; top: 110px; text-align: right; }
  .person-name {
    color: var(--brand-blue);
    font-weight: 500;
    font-size: 15px;
    letter-spacing: 0.5px;
    text-transform: uppercase;
  }
  .person-title { color: var(--title-blue); font-size: 13px; }
  .address {
    position: absolute; right: 28px; top: 160px;
    text-align: right;
    color: var(--ink);
    font-size: 12px;
    line-height: 18px;
  }
  .contacts {
    position: absolute; left: 24px; top: 196px;
    color: var(--ink);
    font-size: 12px;
    letter-spacing: 0.4px;
  }
  .contacts .row { white-space: nowrap; line-height: 22px; }
  .contacts .row-email { padding-left: 270px; }
  .key { color: var(--brand-blue); font-size: 17px; font-weight: 500; margin-right: 3px; }
  .key + .key, .gap { margin-left: 8px; }
  .accent-line {
    position: absolute; left: 0; top: 246px;
    width: 100%; height: 2px;
    background: var(--brand-green);
  }
  .band { position: absolute; left: 0; bottom: 0; width: 540px; height: 50px; }
  /* logo side */
  .card-front {
    display: flex;
    flex-direction: column;
    align-items: center;
    justify-content: center;
    gap: 30px;
  }
  .website { color: var(--ink); font-size: 14px; font-weight: 600; letter-spacing: 1px; }
</style>
</head>
<body>
  <section class="card card-back">
    <div class="brand"><span class="brand-dot"></span>Solvane Energy Group</div>
    <div class="divider"></div>
    <div class="person">
      <p class="person-name">Dustin Garrick</p>
      <p class="person-title">Managing Director</p>
    </div>
    <div class="address">
      <p>214 9th floor Plaza</p>
      <p>Ridge Road NKT</p>
    </div>
    <div class="contacts">
      <p class="row"><span class="key">P</span>012 555 0147<span class="key gap">F</span>012 555 0148</p>
      <p class="row row-email"><span class="key">E</span>dustin@solvane.com</p>
    </div>
    <div class="accent-line"></div>
    <svg class="band" viewBox="0 0 540 50" aria-hidden="true">
      <rect x="0" y="0" width="540" height="50" fill="var(--brand-blue)"/>
      <g fill="var(--card)">
        <rect x="378" y="8" width="7" height="42"/>
        <rect x="404" y="8" width="7" height="42"/>
        <rect x="430" y="8" width="7" height="42"/>
        <rect x="456" y="8" width="7" height="42"/>
        <rect x="482" y="8" width="7" height="42"/>
      </g>
    </svg>
  </section>

  <section class="card card-front">
    <div class="brand"><span class="brand-dot"></span>Solvane Energy Group</div>
    <p class="website">www.solvaneenergy.com</p>
  </section>
</body>
</html>
```